5 post cards for B2B Advertising

We are an electrical lighting contractor advertising our Lighting and Electrical services to property management companies, car dealer ships, hotels, schools, malls, and shopping centers.

RED / White / Blue themed American flag.

Post Cards

1. Electrical Services
2. Lighting Services and conversions to LED
3. Sign Repairs and conversions to LED
4. Nighttime Lighting Inspections (report lights and signs out)
5. Lighting is Safety

```html
<!DOCTYPE html>
<html lang="en">
<head>
<meta charset="utf-8">
<title>Lumen Care Incorporated – Postcard Series</title>
<link href="https://fonts.googleapis.com/css2?family=Anton&family=Open+Sans:wght@400;700&family=Roboto:wght@500;700&display=swap" rel="stylesheet">
<style>
  :root {
    --flag-red: #ec1c24;
    --flag-blue: #27348b;
    --paper: #ffffff;
    --ink: #231f20;
    --canvas: #ffffff;
  }
  * { box-sizing: border-box; margin: 0; padding: 0; }
  html, body { width: 1200px; height: 1200px; overflow: hidden; background: var(--canvas); }
  .sheet { position: relative; width: 1200px; height: 1200px; }

  .postcard {
    position: absolute; width: 508px; height: 360px;
    background: var(--flag-red);
    box-shadow: 0 3px 6px rgba(0,0,0,.35);
    overflow: hidden;
  }
  .postcard--electrical { left: 89px; top: 42px; }
  .postcard--led { left: 611px; top: 44px; }
  .postcard--signs { left: 333px; top: 420px; }
  .postcard--night { left: 89px; top: 797px; }
  .postcard--safety { left: 611px; top: 797px; }

  .postcard__header {
    position: absolute; left: 0; top: 0; width: 364px; height: 59px;
    background: var(--flag-blue);
  }
  .tagline {
    position: absolute; left: 39px; top: 19px;
    display: flex; gap: 6px; align-items: center;
    font-family: 'Roboto', sans-serif; font-weight: 500; line-height: 12px;
  }
  .tagline__since { color: var(--flag-red); font-size: 12px; text-transform: uppercase; }
  .tagline__since b { display: block; font-size: 15px; font-weight: 700; }
  .tagline__claim { color: var(--paper); font-size: 12px; }
  .tagline__claim b { display: block; font-size: 13px; font-weight: 700; }

  .postcard__photo {
    position: absolute; left: 0; top: 59px; width: 239px; height: 301px;
  }
  .photo--stadium { background: linear-gradient(180deg,#b9cfe0 0%,#5d7a4c 22%,#a39486 45%,#c9c3bf 60%,#3f7a36 85%,#cbbcb8 100%); }
  .photo--technician { background: linear-gradient(160deg,#cfd3cf 0%,#e7e3dc 25%,#c9df2f 50%,#b7cf2b 75%,#6f6f70 100%); }
  .photo--storefront { background: linear-gradient(180deg,#cfd9e6 0%,#b59377 35%,#9b5b3f 60%,#d6d6d6 80%,#8d7c6c 100%); }
  .photo--nightsign { background: linear-gradient(180deg,#6c96ef 0%,#8ab4f5 30%,#a8442c 50%,#7e2f1d 78%,#0d0d0d 90%); }
  .photo--polelight { background: linear-gradient(180deg,#5e8bf3 0%,#7aa5f5 40%,#d6da3c 60%,#e8e4da 85%,#6f90e9 100%); }

  .postcard__panel {
    position: absolute; left: 239px; top: 14px; width: 255px; height: 332px;
    background: var(--paper); border-top-left-radius: 16px;
  }
  .brand {
    position: absolute; left: 0; right: 0; top: 14px; text-align: center;
    font-family: 'Anton', sans-serif; color: var(--flag-red);
    text-transform: uppercase; line-height: 1;
  }
  .brand__name { display: block; font-size: 30px; letter-spacing: .5px; }
  .brand__suffix { display: block; font-size: 12px; letter-spacing: .6px; margin-top: 3px; }

  .service-title {
    position: absolute; left: 10px; right: 10px; top: 92px; text-align: center;
    font-family: 'Anton', sans-serif; color: var(--flag-blue);
    font-size: 18px; line-height: 22px; text-transform: uppercase; letter-spacing: .2px;
  }
  .service-title small { display: block; font-size: 10px; line-height: 12px; }
  .service-copy {
    position: absolute; left: 20px; right: 14px;
    font-family: 'Open Sans', sans-serif; color: var(--ink);
    font-size: 9.6px; line-height: 13px; text-align: justify;
  }
  .service-copy b { font-weight: 700; }
  .service-copy--1line { top: 122px; }
  .service-copy--2line { top: 143px; }
  .service-copy--3line { top: 160px; }

  .contact-phone {
    position: absolute; left: 235px; top: 270px; width: 273px; height: 28px;
    background: var(--flag-blue); color: var(--paper);
    display: flex; align-items: center; gap: 8px; padding-left: 38px;
    font-family: 'Open Sans', sans-serif; font-weight: 700; font-size: 22px; letter-spacing: .3px;
  }
  .contact-phone svg { width: 21px; height: 21px; }
  .contact-lines {
    position: absolute; left: 280px; top: 303px;
    font-family: 'Open Sans', sans-serif; font-weight: 700; font-size: 11px;
    color: var(--flag-red); line-height: 16px;
  }
  .contact-lines li { list-style: none; display: flex; align-items: center; gap: 8px; }
  .contact-lines svg { width: 10px; height: 10px; }
</style>
</head>
<body>
<svg width="0" height="0" style="position:absolute">
  <defs>
    <symbol id="icon-phone" viewBox="0 0 24 24">
      <circle cx="12" cy="12" r="10.5" fill="none" stroke="#fff" stroke-width="1.6"/>
      <path d="M9 6.5l1.6 2.6-1.2 1.4c.7 1.6 1.9 2.8 3.4 3.5l1.4-1.2 2.6 1.6-.7 2.2c-4.3-.4-8-4.2-8.4-8.4z" fill="#fff"/>
    </symbol>
    <symbol id="icon-mail" viewBox="0 0 12 12">
      <rect x="1" y="2.5" width="10" height="7" fill="#ec1c24"/>
      <path d="M1 2.5l5 4 5-4M1 9.5l3.5-3.5M11 9.5L7.5 6" stroke="#fff" stroke-width="1" fill="none"/>
    </symbol>
    <symbol id="icon-globe" viewBox="0 0 12 12">
      <g fill="none" stroke="#ec1c24" stroke-width="1">
        <circle cx="6" cy="6" r="5"/><ellipse cx="6" cy="6" rx="2.2" ry="5"/><path d="M1 6h10M2 3.5h8M2 8.5h8"/>
      </g>
    </symbol>
  </defs>
</svg>

<main class="sheet">

  <article class="postcard postcard--electrical">
    <div class="postcard__header"><p class="tagline"><span class="tagline__since">Since<b>1991</b></span><span class="tagline__claim">TRUSTED &amp; RELIABLE<b>LIGHTING EXPERTS</b></span></p></div>
    <div class="postcard__photo photo--stadium" role="img" aria-label="Aerial photo of a football stadium with stands and a green field"></div>
    <section class="postcard__panel">
      <p class="brand"><span class="brand__name">Lumen Care</span><span class="brand__suffix">Incorporated</span></p>
      <h2 class="service-title" style="top:96px">Electrical Services</h2>
      <p class="service-copy service-copy--1line" style="top:127px">At LCI, we offer a wide range of commercial electrical services, so your property, parking lot, retail store, street lights, or other essential electrical systems can continue performing at peak efficiency. From <b>minor repairs</b> and <b>regular maintenance</b> to <b>entire overhauls</b> of your existing electrical system, Lumen Care Inc. treats each and every commercial electrical project with top priority.</p>
    </section>
    <p class="contact-phone"><svg><use href="#icon-phone"/></svg>877 555 0148</p>
    <ul class="contact-lines"><li><svg><use href="#icon-mail"/></svg>info@lumencare-example.com</li><li><svg><use href="#icon-globe"/></svg>www.lumencare-example.com</li></ul>
  </article>

  <article class="postcard postcard--led">
    <div class="postcard__header"><p class="tagline"><span class="tagline__since">Since<b>1991</b></span><span class="tagline__claim">TRUSTED &amp; RELIABLE<b>LIGHTING EXPERTS</b></span></p></div>
    <div class="postcard__photo photo--technician" role="img" aria-label="Photo of a technician in a hard hat and safety shirt servicing an interior light fixture"></div>
    <section class="postcard__panel">
      <p class="brand"><span class="brand__name">Lumen Care</span><span class="brand__suffix">Incorporated</span></p>
      <h2 class="service-title">Lighting Services &amp;<br>Conversions to LED</h2>
      <p class="service-copy service-copy--2line">We offer interior <b>lighting repairs, retrofits, lighting design and group servicing</b> to all our customers. We have lighting technicians available to assist you with interior lighting projects, from <b>installing new fixtures to a complete energy saving retrofit</b>. Lumen Care Inc. is available on an as-needed basis or as part of a full maintenance and management contract.</p>
    </section>
    <p class="contact-phone"><svg><use href="#icon-phone"/></svg>877 555 0148</p>
    <ul class="contact-lines"><li><svg><use href="#icon-mail"/></svg>info@lumencare-example.com</li><li><svg><use href="#icon-globe"/></svg>www.lumencare-example.com</li></ul>
  </article>

  <article class="postcard postcard--signs">
    <div class="postcard__header"><p class="tagline"><span class="tagline__since">Since<b>1991</b></span><span class="tagline__claim">TRUSTED &amp; RELIABLE<b>LIGHTING EXPERTS</b></span></p></div>
    <div class="postcard__photo photo--storefront" role="img" aria-label="Photo of a technician in a bucket lift repairing a restaurant wall sign above a white pickup truck"></div>
    <section class="postcard__panel">
      <p class="brand"><span class="brand__name">Lumen Care</span><span class="brand__suffix">Incorporated</span></p>
      <h2 class="service-title">Sign Repairs &amp;<br>Conversions to LED</h2>
      <p class="service-copy service-copy--2line">Whether you need neon <b>sign repair, large pole sign maintenance</b>, or even <b>LED sign repair</b>, we are trained to find problems big or small and repair them quickly and efficiently.<br>We provide service to <b>neon, fluorescent, LED and pylon signs.</b></p>
    </section>
    <p class="contact-phone"><svg><use href="#icon-phone"/></svg>877 555 0148</p>
    <ul class="contact-lines"><li><svg><use href="#icon-mail"/></svg>info@lumencare-example.com</li><li><svg><use href="#icon-globe"/></svg>www.lumencare-example.com</li></ul>
  </article>

  <article class="postcard postcard--night">
    <div class="postcard__header"><p class="tagline"><span class="tagline__since">Since<b>1991</b></span><span class="tagline__claim">TRUSTED &amp; RELIABLE<b>LIGHTING EXPERTS</b></span></p></div>
    <div class="postcard__photo photo--nightsign" role="img" aria-label="Photo of an illuminated restaurant sign on a curved facade at dusk"></div>
    <section class="postcard__panel">
      <p class="brand"><span class="brand__name">Lumen Care</span><span class="brand__suffix">Incorporated</span></p>
      <h2 class="service-title">Nighttime Lighting<br>Inspections<small>(Report lights and signs out)</small></h2>
      <p class="service-copy service-copy--3line">One of the most popular services that we offer at Lumen Care is night inspections. Our initial visit will identify all of your light locations including <b>wall lights, building mounted signs, as well as pylon signs.</b></p>
    </section>
    <p class="contact-phone"><svg><use href="#icon-phone"/></svg>877 555 0148</p>
    <ul class="contact-lines"><li><svg><use href="#icon-mail"/></svg>info@lumencare-example.com</li><li><svg><use href="#icon-globe"/></svg>www.lumencare-example.com</li></ul>
  </article>

  <article class="postcard postcard--safety">
    <div class="postcard__header"><p class="tagline"><span class="tagline__since">Since<b>1991</b></span><span class="tagline__claim">TRUSTED &amp; RELIABLE<b>LIGHTING EXPERTS</b></span></p></div>
    <div class="postcard__photo photo--polelight" role="img" aria-label="Photo of a technician in a bucket truck servicing a pole light against a blue sky"></div>
    <section class="postcard__panel">
      <p class="brand"><span class="brand__name">Lumen Care</span><span class="brand__suffix">Incorporated</span></p>
      <h2 class="service-title" style="top:96px">Lighting is Safety</h2>
      <p class="service-copy service-copy--1line" style="top:130px">LCI became a proud member of the <b>Regional Safety Alliance</b> to ensure we maintain the high expectations set forth. We proactively develop programs and practices that prevent hazards from ever entering into our workplace. This allows our employees to work at an elevated level of safety and protection, never being exposed to some hazards.</p>
    </section>
    <p class="contact-phone"><svg><use href="#icon-phone"/></svg>877 555 0148</p>
    <ul class="contact-lines"><li><svg><use href="#icon-mail"/></svg>info@lumencare-example.com</li><li><svg><use href="#icon-globe"/></svg>www.lumencare-example.com</li></ul>
  </article>

</main>
</body>
</html>
```